Stationary for Green cleaners and green products
Fresh Leaf Laundry n Goods
Stationary for Green cleaners and green products - Retailers
Creative Brief
Use same font as used in my logo
Harold J Benton
President
4730 Maple Row Millbrook, OH 45999
606-514-7720 or 514-7721
1freshleaflaundry@mailbox-example.com
freshleaflaundry-example.org or.net or .biz
logo also being developed at this site
list of services Dry Cleaning Laundry household items, draperies, leather, wedding gowns, full alterations services green friendly products
Concepts
Business Cards/Letterhead/ Envelopes/Notepads/Tshirt/labels for little big box
Business Card for Womens Clothing Boutique

```html
<!DOCTYPE html>
<html lang="en">
<head>
<meta charset="utf-8">
<title>Fresh Leaf Laundry n Goods – Business Cards</title>
<link href="https://fonts.googleapis.com/css2?family=Open+Sans:wght@400;600&display=swap" rel="stylesheet">
<style>
  :root {
    --bg: #e6e8e7;
    --card: #ffffff;
    --green: #3f9a36;
    --green-dark: #2d7a2a;
    --text-soft: #5f7a55;
    --rule: #c9d8c3;
  }
  * { box-sizing: border-box; margin: 0; padding: 0; }
  html, body { width: 1200px; height: 1009px; overflow: hidden; }
  body {
    background: var(--bg);
    font-family: "Open Sans", sans-serif;
    display: flex;
    flex-direction: column;
    align-items: center;
    justify-content: center;
    gap: 44px;
  }
  .card {
    width: 770px;
    height: 440px;
    background: var(--card);
    border-radius: 26px;
    box-shadow: 0 6px 18px rgba(0,0,0,.12);
    position: relative;
  }
  .brand {
    display: flex;
    align-items: center;
    gap: 14px;
    color: var(--green);
    font-weight: 600;
    font-size: 34px;
    letter-spacing: .2px;
  }
  .brand-dot {
    width: 38px; height: 38px;
    border-radius: 50%;
    background: var(--green);
    flex: none;
  }
  .card-back {
    display: flex;
    flex-direction: column;
    align-items: center;
    justify-content: center;
    gap: 36px;
  }
  .services {
    text-align: center;
    color: var(--green-dark);
    font-size: 17px;
    line-height: 1.55;
  }
  .card-front .brand {
    position: absolute;
    top: 70px;
    left: 0; right: 0;
    justify-content: center;
    font-size: 30px;
  }
  .card-front .brand-dot { width: 34px; height: 34px; }
  .holder {
    position: absolute;
    left: 70px;
    top: 210px;
  }
  .holder-name { color: var(--green); font-size: 26px; font-weight: 600; }
  .holder-title { color: var(--green); font-size: 19px; margin-bottom: 24px; }
  .holder-address { color: var(--text-soft); font-size: 17px; line-height: 1.5; }
  .divider {
    position: absolute;
    left: 335px;
    top: 200px;
    width: 1px;
    height: 180px;
    background: var(--rule);
  }
  .contacts {
    position: absolute;
    left: 365px;
    top: 200px;
    list-style: none;
    color: var(--green-dark);
    font-size: 16px;
  }
  .contacts li {
    display: flex;
    align-items: center;
    gap: 10px;
    height: 30px;
    white-space: nowrap;
  }
  .contacts svg { width: 16px; height: 16px; flex: none; fill: var(--green); }
</style>
</head>
<body>

<section class="card card-back" aria-label="Business card back">
  <div class="brand"><span class="brand-dot"></span>Fresh Leaf Laundry n Goods</div>
  <p class="services">
    Dry Cleaning<br>
    Laundry<br>
    Household Items, Draperies, Leather, Wedding Gowns, Full Alterations Services<br>
    Green Friendly Products
  </p>
</section>

<section class="card card-front" aria-label="Business card front">
  <div class="brand"><span class="brand-dot"></span>Fresh Leaf Laundry n Goods</div>

  <div class="holder">
    <p class="holder-name">Harold J Benton</p>
    <p class="holder-title">President</p>
    <p class="holder-address">4730 Maple Row<br>Millbrook, OH 45999</p>
  </div>

  <div class="divider"></div>

  <ul class="contacts">
    <li><svg viewBox="0 0 24 24"><path d="M6.6 10.8a15 15 0 0 0 6.6 6.6l2.2-2.2a1 1 0 0 1 1-.25 11.4 11.4 0 0 0 3.6.57 1 1 0 0 1 1 1V20a1 1 0 0 1-1 1A17 17 0 0 1 3 4a1 1 0 0 1 1-1h3.5a1 1 0 0 1 1 1c0 1.25.2 2.45.57 3.57a1 1 0 0 1-.25 1z"/></svg>606-514-7720</li>
    <li><svg viewBox="0 0 24 24"><path d="M6.6 10.8a15 15 0 0 0 6.6 6.6l2.2-2.2a1 1 0 0 1 1-.25 11.4 11.4 0 0 0 3.6.57 1 1 0 0 1 1 1V20a1 1 0 0 1-1 1A17 17 0 0 1 3 4a1 1 0 0 1 1-1h3.5a1 1 0 0 1 1 1c0 1.25.2 2.45.57 3.57a1 1 0 0 1-.25 1z"/></svg>606-514-7721</li>
    <li><svg viewBox="0 0 24 24"><path d="M6.6 10.8a15 15 0 0 0 6.6 6.6l2.2-2.2a1 1 0 0 1 1-.25 11.4 11.4 0 0 0 3.6.57 1 1 0 0 1 1 1V20a1 1 0 0 1-1 1A17 17 0 0 1 3 4a1 1 0 0 1 1-1h3.5a1 1 0 0 1 1 1c0 1.25.2 2.45.57 3.57a1 1 0 0 1-.25 1z"/></svg>606-555-0142</li>
    <li><svg viewBox="0 0 24 24"><path d="M6.6 10.8a15 15 0 0 0 6.6 6.6l2.2-2.2a1 1 0 0 1 1-.25 11.4 11.4 0 0 0 3.6.57 1 1 0 0 1 1 1V20a1 1 0 0 1-1 1A17 17 0 0 1 3 4a1 1 0 0 1 1-1h3.5a1 1 0 0 1 1 1c0 1.25.2 2.45.57 3.57a1 1 0 0 1-.25 1z"/></svg>606-555-0187</li>
    <li><svg viewBox="0 0 24 24"><path d="M3 5h18a1 1 0 0 1 1 1v12a1 1 0 0 1-1 1H3a1 1 0 0 1-1-1V6a1 1 0 0 1 1-1zm1 2.2V17h16V7.2l-8 5.3z"/></svg>1freshleaflaundry@mailbox-example.com</li>
    <li><svg viewBox="0 0 24 24"><path d="M12 2a10 10 0 1 0 0 20 10 10 0 0 0 0-20zm0 2c.9 0 2.2 1.8 2.8 5H9.2C9.8 5.8 11.1 4 12 4zM4.3 11h3.8a17 17 0 0 0 0 2H4.3a8 8 0 0 1 0-2zm5 0h5.4a15 15 0 0 1 0 2H9.3a15 15 0 0 1 0-2zm6.6 0h3.8a8 8 0 0 1 0 2h-3.8a17 17 0 0 0 0-2zM9.2 15h5.6c-.6 3.2-1.9 5-2.8 5s-2.2-1.8-2.8-5z"/></svg>www.freshleaflaundry-example.org</li>
  </ul>
</section>

</body>
</html>
```